Wine Bottle Label Graphic Design (mini bottle 187ml)

Looking for a contemporary custom wine label design for party favors. Inspiration photos provided. **Please see "wine favorite" example in uploads.

Artwork 2.5" wide by 2.75" tall to be placed on 3"x3" stickers. Specs from printer attached but I still want image to fit within the artwork size I specified. Please make label center justified. This is for BOYS. It does not need to be super "masculine"...but definitely not feminine.

Required elements:

Colors: white background, include gold and purple to match logo. Other colors are fine to include.

Name: Toviah 13 (I like use of the No) as shown in the sample, but not required
Varietal: Mitzvah Blend 6.11.2021
Vineyard: Brockel Family Vineyard
Location: Maryland
Logo: See attached (KRNotecard Final)

Serif
Sans Serif

• All the above elements. Clean and crisp design. Contemporary and classy. Purple, Gold, Black colors. See logo. You CAN include cursive font for select elements. I don't mind a combination of print and script.
• Floral, scrolling, background image, old fashioned

```html
<!DOCTYPE html>
<html lang="en">
<head>
<meta charset="utf-8">
<title>Toviah 13 – Mitzvah Blend Label</title>
<link rel="stylesheet" href="https://fonts.googleapis.com/css2?family=Libre+Caslon+Text:wght@400;700&family=Pinyon+Script&family=Playfair+Display:wght@700&display=swap">
<style>
  :root {
    --backdrop: #efeee6;
    --label-white: #ffffff;
    --gold: #c9a54b;
    --gold-deep: #a8832c;
    --purple: #3d2f86;
    --ink: #1c1d3a;
  }
  * { margin: 0; padding: 0; box-sizing: border-box; }
  html, body {
    width: 1200px; height: 1200px; overflow: hidden;
    background: var(--backdrop);
  }
  .label {
    position: absolute;
    left: 320px; top: 210px;
    width: 560px; height: 780px;
  }
  .label-shape { position: absolute; inset: 0; }
  .label-content {
    position: absolute; inset: 0;
    display: flex; flex-direction: column; align-items: center;
    text-align: center; color: var(--ink);
    font-family: "Libre Caslon Text", serif;
  }
  .brand {
    margin-top: 58px;
    display: flex; align-items: center; gap: 14px;
  }
  .brand-dot {
    width: 34px; height: 34px; border-radius: 50%;
    background: var(--purple);
  }
  .brand-name {
    font-family: "Libre Caslon Text", serif;
    font-weight: 700; font-size: 26px; letter-spacing: 3px;
    text-transform: uppercase; color: var(--purple);
  }
  .vineyard {
    margin-top: 70px;
    font-size: 15px; letter-spacing: 2px; text-transform: uppercase;
  }
  .wine-name {
    margin-top: 18px;
    font-family: "Pinyon Script", cursive;
    font-size: 92px; line-height: 1; color: var(--ink);
  }
  .wine-number {
    font-family: "Playfair Display", serif;
    font-weight: 700; font-size: 96px; line-height: 1;
    color: var(--ink); margin-top: 2px;
  }
  .gold-rule {
    margin-top: 14px; width: 300px; height: 16px;
  }
  .varietal {
    margin-top: 10px;
    font-size: 20px; letter-spacing: 3px; text-transform: uppercase;
  }
  .vintage {
    margin-top: 8px;
    font-size: 18px; letter-spacing: 14px; padding-left: 14px;
  }
  .origin {
    margin-top: 58px;
    display: flex; align-items: baseline; gap: 10px;
    font-family: "Pinyon Script", cursive; color: var(--ink);
  }
  .origin-small { font-size: 26px; }
  .origin-place { font-size: 58px; }
</style>
</head>
<body>
  <section class="label" aria-label="Toviah 13 Mitzvah Blend wine label">
    <svg class="label-shape" viewBox="0 0 560 780" aria-hidden="true">
      <path d="M0,200 C0,80 130,0 280,0 C430,0 560,80 560,200 L560,720 Q536,720 536,744 L536,780 L24,780 L24,744 Q24,720 0,720 Z"
            fill="var(--label-white)"/>
      <path d="M16,204 C16,92 140,16 280,16 C420,16 544,92 544,204 L544,706 Q522,708 520,732 L520,764 L40,764 L40,732 Q38,708 16,706 Z"
            fill="none" stroke="var(--gold)" stroke-width="2"/>
    </svg>
    <div class="label-content">
      <div class="brand">
        <span class="brand-dot"></span>
        <span class="brand-name">Kai and Rowan</span>
      </div>
      <p class="vineyard">Brockel Family Vineyard</p>
      <h1 class="wine-name">Toviah</h1>
      <p class="wine-number">13</p>
      <svg class="gold-rule" viewBox="0 0 300 16" aria-hidden="true">
        <line x1="0" y1="8" x2="300" y2="8" stroke="var(--gold-deep)" stroke-width="1.5"/>
        <line x1="20" y1="0" x2="20" y2="16" stroke="var(--gold)" stroke-width="1.5"/>
        <line x1="280" y1="0" x2="280" y2="16" stroke="var(--gold)" stroke-width="1.5"/>
      </svg>
      <p class="varietal">Mitzvah Blend</p>
      <p class="vintage">2·0·2·1</p>
      <p class="origin">
        <span class="origin-small">Made in</span>
        <span class="origin-place">Maryland</span>
      </p>
    </div>
  </section>
</body>
</html>
```